Birchford Realty Business Card

Business Card:

Somewhere on front of card, please include Broker License Number: 5839162

Website is BirchfordRealty.example

Address is:
7218 Crestover Ave E
Alderton, OH 48271

I'll let you use creative freedom on the rest; we obviously need Name, Title, Email (@BirchfordRealty.example), Office Phone, Cell Phone.

Don't want any special die-cutting, just a standard size business card.

On the back, include a place for the date and time of an appointment to be written in pen.

Requirements
Must have
• Our logo, attached to email.

```html
<!DOCTYPE html>
<html lang="en">
<head>
<meta charset="utf-8">
<title>Birchford Realty Business Card</title>
<link rel="stylesheet" href="https://fonts.googleapis.com/css2?family=Ubuntu:wght@400;500;700&display=swap">
<style>
  :root {
    --backdrop: #8a8b8c;
    --card: #e9eaec;
    --navy: #27286e;
    --band-grey: #bcbdc0;
    --rule: #3c3d55;
    --ink: #4a4b52;
    --muted: #5d5e63;
  }
  * { margin: 0; padding: 0; box-sizing: border-box; }
  html, body {
    width: 1200px; height: 900px; overflow: hidden;
    background: var(--backdrop);
    font-family: "Ubuntu", sans-serif;
  }
  .canvas { position: relative; width: 1200px; height: 900px; }
  .card {
    position: absolute; left: 262px;
    width: 676px; height: 386px;
    background: var(--card);
  }
  .card--back { top: 39px; }
  .card--front { top: 475px; }

  /* Back: appointment slip */
  .field-label {
    position: absolute; top: 59px;
    font-size: 19px; color: var(--navy);
  }
  .field-label--date { left: 41px; }
  .field-label--time { left: 376px; }
  .field-suffix {
    position: absolute; top: 65px; right: 51px;
    font-size: 14px; color: var(--navy);
  }
  .rule { position: absolute; height: 1.5px; background: var(--rule); }
  .rule--date { left: 42px; width: 313px; top: 88px; }
  .rule--time { left: 380px; width: 245px; top: 88px; }
  .rule--note { left: 45px; width: 583px; }
  .back-site {
    position: absolute; left: 0; right: 0; top: 339px;
    text-align: center; font-size: 16px; letter-spacing: 3px;
    color: var(--muted);
  }

  /* Front */
  .brand-name {
    position: absolute; left: 38px; top: 60px;
    font-size: 46px; font-weight: 700; color: var(--navy);
    letter-spacing: -0.5px;
  }
  .name-band { position: absolute; left: 0; top: 176px; width: 676px; height: 67px; }
  .person { position: absolute; left: 40px; top: 184px; color: #fff; }
  .person-name { font-size: 25px; font-weight: 700; line-height: 1.1; }
  .person-title { font-size: 18px; font-weight: 400; line-height: 1.3; }
  .contact-list { position: absolute; left: 36px; top: 258px; list-style: none; }
  .contact-item {
    display: flex; align-items: center; height: 26px;
    font-size: 17px; color: var(--ink);
  }
  .contact-icon { width: 16px; height: 16px; margin-right: 9px; fill: var(--navy); }
  .office-details {
    position: absolute; right: 37px; top: 289px;
    text-align: right; font-size: 17px; line-height: 22px; color: var(--ink);
    font-style: normal;
  }
</style>
</head>
<body>
<main class="canvas">

  <section class="card card--back" aria-label="Card back: appointment">
    <span class="field-label field-label--date">Date :</span>
    <span class="rule rule--date"></span>
    <span class="field-label field-label--time">Time :</span>
    <span class="field-suffix">AM/PM</span>
    <span class="rule rule--time"></span>
    <span class="rule rule--note" style="top:141px"></span>
    <span class="rule rule--note" style="top:198px"></span>
    <span class="rule rule--note" style="top:250px"></span>
    <span class="rule rule--note" style="top:301px"></span>
    <p class="back-site">www.BirchfordRealty.example</p>
  </section>

  <section class="card card--front" aria-label="Card front">
    <h1 class="brand-name">Birchford Realty</h1>

    <svg class="name-band" viewBox="0 0 676 67" aria-hidden="true">
      <polygon points="0,0 510,0 481,67 0,67" fill="var(--navy)"/>
      <polygon points="522,0 676,0 676,67 493,67" fill="var(--band-grey)"/>
    </svg>
    <div class="person">
      <p class="person-name">Evan Hartley</p>
      <p class="person-title">CEO/Founder</p>
    </div>

    <ul class="contact-list">
      <li class="contact-item">
        <svg class="contact-icon" viewBox="0 0 16 16" aria-hidden="true"><path d="M3.2 1l2.6 3-1.3 1.6c.9 2 2.6 3.7 4.6 4.6l1.6-1.3 3 2.6-1.2 2.5C6.4 14.3 1.7 9.6 1.5 3.5z"/></svg>
        555 014 2276
      </li>
      <li class="contact-item">
        <svg class="contact-icon" viewBox="0 0 16 16" aria-hidden="true"><path d="M4 0h8a1 1 0 0 1 1 1v14a1 1 0 0 1-1 1H4a1 1 0 0 1-1-1V1a1 1 0 0 1 1-1zm1 2v10h6V2zm3 11a1 1 0 1 0 0 2 1 1 0 0 0 0-2z"/></svg>
        555 019 7431
      </li>
      <li class="contact-item">
        <svg class="contact-icon" viewBox="0 0 16 16" aria-hidden="true"><path d="M1 4h14v9H1zm1.5 1L8 9l5.5-4z" fill-rule="evenodd"/></svg>
        name@BirchfordRealty.example
      </li>
      <li class="contact-item">
        <svg class="contact-icon" viewBox="0 0 16 16" aria-hidden="true"><circle cx="8" cy="8" r="7"/><path d="M8 1.5v13M1.5 8h13M8 1.5c-3 3-3 10 0 13M8 1.5c3 3 3 10 0 13" stroke="#e9eaec" stroke-width="1.1" fill="none"/></svg>
        www.BirchfordRealty.example
      </li>
    </ul>

    <address class="office-details">
      Broker Lic No: 5839162<br>
      7218 Crestover Ave E<br>
      Alderton, OH 48271
    </address>
  </section>

</main>
</body>
</html>
```